Create a channel art for human resources youtube channel

We a are human resource company that want to develop a community on youtube. Our channel is call "PVK Studio" and we will produce videos related to human resources topics like: Strategy, Job Description, selection of workers, workers development, Occupational health, Training, etc.

We need a channel art for our youtube channel that communicate to our viewers what is about the channel.

Attach you can see the logo and icon of the channel, also you can see it here: https://www.vidlumo.example/channel/UCqTbWxe7Rk3LmNpaVhyOdZZ

Target Market(s)

The people who is going to see the art - banner for youtube are persons that work on human resources field

Industry/Entity Type

Business

Font styles to use
Sans Serif

Requirements
Must have
• Must to communicate that our channel is about how to do a better and faster human resources to help business improve there productivity , also workers performances and quality work life. Here are some key words to help you inspire:
• Human Resources
• Performance
• Better
• Faster
• Easier
• Business
• Improve
• Health

```html
<!DOCTYPE html>
<html lang="en">
<head>
<meta charset="utf-8">
<title>PVK Studio – Channel Banner</title>
<link rel="stylesheet" href="https://fonts.googleapis.com/css2?family=Roboto:wght@300&display=swap">
<style>
  :root {
    --ink-dark: #141618;
    --ink-mid: #2a2d30;
    --ink-light: #3b3e41;
    --blue-deep: #0b4f9c;
    --blue-mid: #1670c4;
    --blue-bright: #2e95db;
    --headline: #ffffff;
  }
  html, body {
    margin: 0;
    padding: 0;
    width: 1200px;
    height: 205px;
    overflow: hidden;
    background: var(--ink-dark);
  }
  .banner {
    position: relative;
    width: 1200px;
    height: 205px;
    overflow: hidden;
  }
  .banner__city {
    position: absolute;
    inset: 0;
    background:
      linear-gradient(90deg, var(--ink-dark) 0%, var(--ink-mid) 45%, var(--ink-light) 75%, var(--ink-mid) 100%),
      var(--ink-dark);
  }
  .banner__mosaic {
    position: absolute;
    left: 0;
    top: 0;
    width: 470px;
    height: 205px;
  }
  .banner__headline {
    position: absolute;
    left: 502px;
    top: 72px;
    margin: 0;
    font-family: "Roboto", sans-serif;
    font-weight: 300;
    font-size: 35px;
    line-height: 32px;
    letter-spacing: -0.6px;
    color: var(--headline);
    white-space: nowrap;
  }
  .banner__headline span {
    display: block;
  }
</style>
</head>
<body>
  <div class="banner">
    <div class="banner__city" role="img" aria-label="Dark aerial photograph of downtown office rooftops"></div>

    <svg class="banner__mosaic" viewBox="0 0 470 205" role="img" aria-label="Blue diamond tile pattern">
      <defs>
        <linearGradient id="mosaic-fill" x1="0" y1="0" x2="1" y2="1">
          <stop offset="0" stop-color="var(--blue-deep)"/>
          <stop offset="0.55" stop-color="var(--blue-mid)"/>
          <stop offset="1" stop-color="var(--blue-bright)"/>
        </linearGradient>
      </defs>
      <polygon points="0,0 392,0 465,72 440,112 455,140 410,205 0,205" fill="url(#mosaic-fill)"/>
    </svg>

    <h1 class="banner__headline">
      <span>HR Tips &amp; Tricks To Help Your Business</span>
      <span>Improve Productivity and Performance</span>
    </h1>
  </div>
</body>
</html>
```